Need a sleek, professional business card design for a Web Development business

I need a unique business card designed for a web development company. It is also the parent company for any ventures I do, such as my ClipWave channel, startup ideas I have, etc. I am the single member of "Bright Harbor Code LLC." I will attach my basic logo here, so you will see the current color scheme and have the asset available. Thank you!

Target Market(s)

Startups, SMB's, Professionals

Industry/Entity Type

Business

Font styles to use
Other font styles liked:
• Lovello for headings is what I use, but not necessary.

Colors

Designer to choose colors to be used in the design.

Requirements
Nice to have
• Sleek is the word. Professional, modern, dark.
Should not have
• Any work from someone else's design. Lacking originality.

```html
<!DOCTYPE html>
<html lang="en">
<head>
<meta charset="utf-8">
<title>Bright Harbor Code LLC — Business Card</title>
<link rel="stylesheet" href="https://fonts.googleapis.com/css2?family=Michroma&display=swap">
<style>
  :root {
    --backdrop: #e4e4e4;
    --panel: #1d1c19;
    --ink-light: #f1f1f1;
    --ink-soft: #d6d6d6;
    --accent: #f2a24e;
    --icon-fill: #8c8c8c;
    --icon-ink: #5a5a5a;
  }
  * { margin: 0; padding: 0; box-sizing: border-box; }
  html, body {
    width: 1200px; height: 827px; overflow: hidden;
    background: var(--backdrop);
  }
  .card {
    position: absolute; left: 150px; top: 156px;
    width: 900px; height: 514px;
    border-radius: 4px; overflow: hidden;
    box-shadow: 0 18px 40px rgba(0,0,0,.28);
    font-family: "Michroma", sans-serif;
  }
  .card-shapes { position: absolute; inset: 0; }
  .brand {
    position: absolute; left: 70px; top: 110px; width: 320px;
    display: flex; flex-direction: column; align-items: center; gap: 20px;
    text-align: center;
  }
  .brand-dot {
    width: 84px; height: 84px; border-radius: 50%;
    background: var(--accent);
  }
  .brand-name {
    color: var(--accent); font-size: 16px; line-height: 1.6;
    letter-spacing: .5px; text-transform: uppercase;
  }
  .identity {
    position: absolute; right: 48px; top: 62px; text-align: right;
  }
  .identity-name {
    color: var(--ink-light); font-size: 34px; letter-spacing: 5px; font-weight: 400;
  }
  .identity-role {
    color: var(--ink-soft); font-size: 15px; letter-spacing: 5px; margin-top: 6px;
  }
  .contacts {
    position: absolute; left: 470px; top: 222px;
    list-style: none; color: var(--ink-light);
  }
  .contact {
    display: flex; align-items: center; gap: 14px; margin-bottom: 18px;
    font-size: 14px; letter-spacing: 2px;
  }
  .contact--phone { font-size: 24px; letter-spacing: 5px; }
  .contact svg { width: 20px; height: 20px; flex: none; fill: var(--ink-light); }
  .socials {
    position: absolute; right: 40px; top: 428px;
    display: flex; gap: 28px; list-style: none;
  }
  .social-dot {
    width: 34px; height: 34px; border-radius: 50%;
    background: var(--icon-fill);
    box-shadow: inset 0 0 0 2px var(--icon-ink);
  }
</style>
</head>
<body>
  <article class="card">
    <svg class="card-shapes" viewBox="0 0 900 514" aria-hidden="true">
      <defs>
        <linearGradient id="frame-metal" x1="0" y1="0" x2="1" y2="1">
          <stop offset="0" stop-color="#7a7a7a"/>
          <stop offset=".55" stop-color="#a7a7a7"/>
          <stop offset="1" stop-color="#8a8a8a"/>
        </linearGradient>
        <linearGradient id="panel-fill" x1="0" y1="0" x2="0" y2="1">
          <stop offset="0" stop-color="#24231f"/>
          <stop offset="1" stop-color="#1a1917"/>
        </linearGradient>
      </defs>
      <rect class="card-frame" width="900" height="514" fill="url(#frame-metal)"/>
      <polygon class="card-frame-shade" points="0,0 560,0 640,175 900,175 900,0" fill="#b5b5b5" opacity=".35"/>
      <polygon class="card-panel" points="28,42 560,42 640,178 900,178 900,412 500,412 455,474 28,474" fill="url(#panel-fill)"/>
    </svg>

    <div class="brand">
      <span class="brand-dot"></span>
      <span class="brand-name">Bright Harbor Code<br>LLC</span>
    </div>

    <header class="identity">
      <h1 class="identity-name">DANIEL REYES</h1>
      <p class="identity-role">GENERAL DIRECTOR</p>
    </header>

    <ul class="contacts">
      <li class="contact contact--phone">
        <svg viewBox="0 0 24 24" aria-hidden="true"><path d="M6.6 10.8a15.1 15.1 0 0 0 6.6 6.6l2.2-2.2c.3-.3.7-.4 1-.2 1.1.4 2.3.6 3.6.6.6 0 1 .4 1 1V20c0 .6-.4 1-1 1A17 17 0 0 1 3 4c0-.6.4-1 1-1h3.5c.6 0 1 .4 1 1 0 1.3.2 2.5.6 3.6.1.3 0 .7-.2 1z"/></svg>
        555.018.2740
      </li>
      <li class="contact">
        <svg viewBox="0 0 24 24" aria-hidden="true"><path d="M3 5h18v14H3zm2 2v.4l7 4.6 7-4.6V7zm0 2.8V17h14V9.8l-7 4.6z"/></svg>
        daniel.reyes@bhc.com
      </li>
      <li class="contact">
        <svg viewBox="0 0 24 24" aria-hidden="true"><path d="M12 2a10 10 0 1 0 0 20 10 10 0 0 0 0-20zm6.9 6h-3a15 15 0 0 0-1.3-3.9A8 8 0 0 1 18.9 8zM12 4c.8 1.1 1.5 2.5 1.9 4h-3.8c.4-1.5 1.1-2.9 1.9-4zM4.3 14a8 8 0 0 1 0-4h3.4a16 16 0 0 0 0 4zm.8 2h3a15 15 0 0 0 1.3 3.9A8 8 0 0 1 5.1 16zm3-8h-3a8 8 0 0 1 4.3-3.9A15 15 0 0 0 8.1 8zM12 20c-.8-1.1-1.5-2.5-1.9-4h3.8c-.4 1.5-1.1 2.9-1.9 4zm2.3-6H9.7a14 14 0 0 1 0-4h4.6a14 14 0 0 1 0 4zm.3 5.900a15 15 0 0 0 1.3-3.9h3a8 8 0 0 1-4.3 3.9zm1.7-5.9a16 16 0 0 0 0-4h3.4a8 8 0 0 1 0 4z"/></svg>
        www.brightharborcode.com
      </li>
    </ul>

    <ul class="socials" aria-label="Social channels">
      <li class="social-dot" aria-label="ClipWave"></li>
      <li class="social-dot"></li>
      <li class="social-dot"></li>
      <li class="social-dot"></li>
      <li class="social-dot"></li>
    </ul>
  </article>
</body>
</html>
```